Medical Staffing Pamphlet

We are starting to staff for Medical positions for the first time, we need pamphlets to take to medical facilities to try to gain new business

Need an copy to edit, many errors.

```html
<!DOCTYPE html>
<html lang="en">
<head>
<meta charset="utf-8">
<title>Medical Staffing Pamphlet</title>
<link rel="stylesheet" href="https://fonts.googleapis.com/css2?family=Josefin+Sans:wght@400;600;700&family=Noto+Serif:wght@400&display=swap">
<style>
  :root {
    --green: #5e8c46;
    --green-light: #6fa84a;
    --navy: #1f3f66;
    --navy-deep: #2c3f78;
    --white: #ffffff;
    --stage: #e8edf3;
    --photo-a: #dfe8ef;
    --photo-b: #2a63a8;
    --photo-c: #1f8a9e;
  }
  * { box-sizing: border-box; margin: 0; padding: 0; }
  html, body { width: 1200px; height: 900px; overflow: hidden; }
  body { background: var(--stage); font-family: "Josefin Sans", sans-serif; }

  .pamphlet {
    position: absolute; left: 50px; top: 150px;
    width: 1100px; height: 600px;
    background: var(--white);
    box-shadow: 0 14px 40px rgba(31,63,102,.25);
    overflow: hidden;
  }
  .intro {
    position: absolute; left: 0; top: 0;
    width: 420px; height: 290px;
    background: var(--green); color: var(--white);
    padding: 40px 48px 0 64px;
  }
  .intro-title { font-size: 25px; font-weight: 600; letter-spacing: .5px; margin-bottom: 10px; }
  .intro-text { font-size: 15.5px; line-height: 1.42; letter-spacing: .8px; }

  .team-photo {
    position: absolute; left: 420px; top: 0;
    width: 680px; height: 290px;
    background: linear-gradient(100deg, var(--photo-b) 0%, var(--photo-c) 38%, var(--photo-a) 62%, #f4f7f9 100%);
  }

  .services-title {
    position: absolute; left: 130px; top: 340px;
    font-size: 34px; font-weight: 700; color: var(--navy); letter-spacing: .5px;
    line-height: 1;
  }
  .services-rule {
    position: absolute; left: 134px; top: 384px;
    width: 150px; height: 4px; background: var(--navy);
  }

  .column { position: absolute; top: 410px; }
  .column-admin { left: 180px; }
  .column-clinical { left: 520px; top: 420px; }
  .column-title {
    font-size: 26px; font-weight: 600; color: var(--green); line-height: 1.1;
    text-decoration: underline; text-underline-offset: 4px; text-decoration-thickness: 2px;
    margin-bottom: 16px;
  }
  .service-list { list-style: none; color: var(--navy); font-size: 15px; line-height: 1.5; letter-spacing: .8px; }
  .column-admin .service-list { padding-left: 10px; }
  .column-clinical .service-list { padding-left: 14px; }

  .divider {
    position: absolute; left: 462px; top: 410px;
    width: 2px; height: 150px; background: var(--navy);
  }

  .stethoscope { position: absolute; left: 640px; top: 312px; }
  .tagline {
    position: absolute; left: 760px; top: 310px; width: 300px;
    font-family: "Noto Serif", serif; font-size: 14px; line-height: 1.35;
    letter-spacing: 1.4px; color: #1d1d1d;
  }

  .corner-stripes { position: absolute; right: 0; bottom: 0; }
</style>
</head>
<body>
  <main class="pamphlet">
    <section class="intro">
      <h2 class="intro-title">WHO WE ARE</h2>
      <p class="intro-text">Keystone Staffing is the largest locally owned recruiting company in the Tri-State.We began building staffing partnerships are the foundation of our success.We provide customized staffing solutions for the many industries &amp; services including medical.</p>
    </section>

    <div class="team-photo" role="img" aria-label="Photo of three medical staff in scrubs reviewing an X-ray together"></div>

    <h1 class="services-title">OUR SERVICES</h1>
    <div class="services-rule"></div>

    <section class="column column-admin">
      <h3 class="column-title">Administrative</h3>
      <ol class="service-list">
        <li>1. Billing Specialists</li>
        <li>2. Coding Specialists</li>
        <li>3. Medical Records</li>
        <li>4. Office Managers</li>
        <li>5. Receptionists</li>
      </ol>
    </section>

    <div class="divider"></div>

    <section class="column column-clinical">
      <h3 class="column-title">Clinical</h3>
      <ol class="service-list">
        <li>1. Certified Medical Assistants</li>
        <li>2 . Registered Medical Assistants</li>
        <li>3. Certified Nursing Assistant</li>
        <li>5. Phlebotomists</li>
      </ol>
    </section>

    <svg class="stethoscope" width="100" height="80" viewBox="0 0 100 80" fill="none" stroke="var(--green)" stroke-width="3" stroke-linecap="round" aria-hidden="true">
      <path d="M10 8 C4 10 4 30 14 40 C20 46 30 46 36 40 C46 30 46 10 40 8"/>
      <circle cx="10" cy="8" r="3"/>
      <circle cx="40" cy="8" r="3"/>
      <path d="M25 45 V58 C25 72 50 74 52 58 V40 C52 30 70 30 72 38"/>
      <circle cx="80" cy="42" r="8"/>
    </svg>
    <p class="tagline">“Put your trust in us &amp; we will take care of your medical staffing needs”</p>

    <svg class="corner-stripes" width="220" height="230" viewBox="0 0 220 230" aria-hidden="true">
      <defs>
        <linearGradient id="stripeNavy" x1="0" y1="1" x2="1" y2="0">
          <stop offset="0" stop-color="#9cb6d6"/>
          <stop offset=".55" stop-color="var(--navy-deep)"/>
          <stop offset="1" stop-color="var(--navy-deep)"/>
        </linearGradient>
      </defs>
      <polygon points="30,230 220,10 220,90 100,230" fill="url(#stripeNavy)"/>
      <polygon points="135,230 220,130 220,230" fill="var(--green-light)"/>
    </svg>
  </main>
</body>
</html>
```